Need a Marketing System Program Overview Flyer

Our business, Builder Summit Network, helps General Contractors and home improvement businesses to generate high quality leads, acquire new customers, and improve their overall online presence.

The system includes a...
- High Converting Website
- SEO & Online Listings Management
- Strategic PPC Advertising
- Email Marketing and Automation
- Social Media Management & Retargeting Campaigns
- Reputation Management
- Tracking and Reporting

The Brochure or flyer needs to have a very professional and high class look that wows the potential customers when overviewing the program.

It needs to give a clear explanation of the program while simultaneously having the very best design concept that pulls the reader in.

I've attached our branding guide, logos and additional information...

Our site is currently being staged at www.lanternvista.com/BSN

```html
<!DOCTYPE html>
<html lang="en">
<head>
<meta charset="utf-8">
<title>Builder Summit Network – Program Overview Flyer</title>
<link rel="stylesheet" href="https://fonts.googleapis.com/css2?family=Montserrat:wght@400;500;600;700&family=Oswald:wght@400;500;600;700&display=swap">
<style>
:root{
  --gold:#c3a865;
  --gold-dark:#a98f4f;
  --ink:#0d0d0d;
  --charcoal:#2b2b2b;
  --paper:#ffffff;
  --mist:#ececec;
  --stage:#4a4a4a;
  --text:#1b1b1b;
}
*{box-sizing:border-box;margin:0;padding:0}
html,body{width:1200px;height:788px;overflow:hidden;background:var(--stage)}
body{position:relative;font-family:"Montserrat",sans-serif;color:var(--text)}
.page{position:absolute;top:66px;width:510px;height:660px;background:var(--paper);overflow:hidden}
.page--front{left:60px}
.page--back{left:629px}
.abs{position:absolute}
.condensed{font-family:"Oswald",sans-serif;text-transform:uppercase}

/* front header */
.front-header{left:0;top:0;width:510px;height:118px;background:var(--paper)}
.brand{left:44px;top:40px;display:flex;align-items:center;gap:10px}
.brand-square{width:22px;height:22px;background:var(--ink)}
.brand-name{font-family:"Montserrat",sans-serif;font-weight:700;font-size:17px;line-height:1.15;color:var(--ink);letter-spacing:.5px;text-transform:uppercase}
.social{left:412px;top:27px;display:flex;gap:6px}
.social span{width:15px;height:15px;border:1.5px solid #fff;border-radius:50%}
.site-url{left:336px;top:51px;font-size:9.5px;color:#fff;font-weight:500;letter-spacing:.2px;white-space:nowrap}

/* hero */
.hero{left:0;top:118px;width:510px;height:249px;background:var(--ink)}
.hero-photo{left:258px;top:0;width:252px;height:249px;background:radial-gradient(ellipse at 60% 65%,#8a7330 0%,#4a3c17 35%,#0d0d0d 75%)}
.hero-copy{left:32px;top:20px;white-space:nowrap}
.hero-line1{font-size:22px;color:#fff;font-weight:400;line-height:1}
.hero-line1 b{font-weight:700}
.hero-line2{font-size:35px;color:var(--gold);font-weight:700;line-height:1;margin-top:5px}
.hero-line3{font-size:23px;color:#fff;font-weight:400;line-height:1;margin-top:6px}
.hero-line3 b{font-weight:700}
.hero-tag{margin-top:8px;display:inline-block;background:var(--gold);border:2px solid #e2cf99;color:var(--ink);font-size:33px;font-weight:700;line-height:1;padding:2px 14px 3px}

/* roi band */
.roi-band{left:0;top:367px;width:510px;height:47px;background:var(--gold);text-align:center}
.roi-band p{font-size:17px;color:#fff;font-weight:600;margin-top:7px;letter-spacing:.1px;white-space:nowrap}
.roi-box{left:108px;top:402px;width:295px;height:28px;background:var(--ink);color:#fff;font-size:17px;font-weight:600;text-align:center;line-height:28px;white-space:nowrap}

/* features */
.features{left:0;top:430px;width:510px;height:192px;background:linear-gradient(135deg,#e3e3e3 0%,#fafafa 45%,#efefef 100%)}
.feature{position:absolute;width:120px;text-align:center}
.feature-icon{width:40px;height:40px;border-radius:50%;background:var(--gold);margin:0 auto 7px;display:flex;align-items:center;justify-content:center;box-shadow:0 0 0 3px rgba(195,168,101,.25)}
.feature-icon svg{width:22px;height:22px;stroke:#fff;fill:none;stroke-width:1.4}
.feature p{font-size:10px;line-height:1.25;color:var(--text);font-weight:500;white-space:nowrap}

/* footer */
.footer{left:0;top:622px;width:510px;height:38px;background:var(--ink);z-index:3}
.footer-cta{position:absolute;left:0;top:0;width:210px;height:38px;background:var(--gold);clip-path:polygon(0 0,186px 0,210px 38px,0 38px)}
.footer-cta span{position:absolute;left:30px;top:11px;font-weight:700;font-size:13.5px;color:var(--ink);letter-spacing:.3px;white-space:nowrap}
.footer-contact{position:absolute;left:214px;top:0;height:38px;display:flex;align-items:center;gap:10px;color:var(--gold);font-weight:600;font-size:13px;white-space:nowrap}
.footer-contact span{display:flex;align-items:center;gap:4px}
.footer-contact svg{width:12px;height:12px;stroke:#fff;fill:none;stroke-width:1.6;flex:none}

/* back page */
.back-top{left:0;top:0;width:510px;height:196px;background:var(--gold)}
.back-top-right{left:0;top:0;width:510px;height:196px;background:#f1f1f1;clip-path:polygon(258px 0,510px 0,510px 196px,350px 196px)}
.question{left:32px;top:28px;width:230px;color:#fff;font-size:13px;line-height:1.25;font-weight:400}
.question b{font-weight:700}
.first-step{left:30px;top:127px;width:210px;height:44px;background:var(--charcoal);border:1px solid #555;color:#fff;font-size:13px;line-height:1.3;padding:5px 0 0 15px;box-shadow:0 2px 4px rgba(0,0,0,.35);white-space:nowrap}
.checklist-art{left:262px;top:24px;width:240px;height:168px;background:linear-gradient(160deg,#f3e7b8 0%,#ddd6c6 45%,#f7f7f7 100%)}
.mission{left:0;top:196px;width:510px;height:117px;background:linear-gradient(180deg,#262626,#1a1a1a)}
.mission p{position:absolute;left:20px;top:20px;width:470px;text-align:center;color:#fff;font-weight:700;font-size:10.3px;line-height:1.55}
.how-tab{left:132px;top:283px;width:248px;height:31px;background:var(--gold);clip-path:polygon(14px 0,234px 0,248px 31px,0 31px);color:#fff;font-size:19px;font-weight:700;text-align:center;line-height:31px}
.steps{left:0;top:314px;width:510px;height:308px;background:linear-gradient(135deg,#f6f6f6,#e7e7e7)}
.step-art{position:absolute;left:44px;width:76px;height:68px;border-radius:4px}
.step-divider{position:absolute;left:149px;width:1.5px;background:var(--gold)}
.step{position:absolute;left:168px;z-index:2}
.step h3{font-size:12.2px;font-weight:500;line-height:1.2;color:var(--text);white-space:nowrap}
.step p{font-size:7.2px;font-weight:600;line-height:1.25;margin-top:5px;color:var(--text);white-space:nowrap}
.portrait{left:352px;top:418px;width:158px;height:204px;background:linear-gradient(180deg,#d8d8d8 0%,#1f3a4a 40%,#132630 100%);border-radius:70px 70px 0 0;z-index:1}
.ready{left:40px;top:586px;width:282px;height:24px;border:1px solid #777;background:#fff;text-align:center;font-size:11.5px;line-height:22px;font-weight:600;color:var(--ink);white-space:nowrap;z-index:2}
.ready em{font-style:normal;color:var(--gold)}
</style>
</head>
<body>

<section class="page page--front">
  <header class="abs front-header">
    <svg class="abs" style="left:0;top:0" width="510" height="118" aria-hidden="true">
      <polygon points="275,0 510,0 510,76 323,76" fill="#c3a865"/>
      <polygon points="262,0 275,0 323,76 310,76" fill="#d9d9d9"/>
    </svg>
    <div class="abs brand">
      <div class="brand-square"></div>
      <div class="brand-name">Builder Summit<br>Network</div>
    </div>
    <div class="abs social" aria-hidden="true"><span></span><span></span><span></span></div>
    <div class="abs site-url">www.lanternvista.com/BSN</div>
  </header>

  <div class="abs hero">
    <div class="abs hero-photo" role="img" aria-label="Photo of miniature construction workers stacking tall columns of gold coins"></div>
    <div class="abs hero-copy condensed">
      <div class="hero-line1"><b>Accelerate</b> your</div>
      <div class="hero-line2">Lead Generation</div>
      <div class="hero-line3">While <b>Increasing Sales</b> and</div>
      <div class="hero-tag">Reducing Costs</div>
    </div>
  </div>

  <div class="abs roi-band condensed"><p>Our 8-Point Builder Summit Network will show you what</p></div>
  <div class="abs roi-box condensed">Return on investment truly means!</div>

  <div class="abs features">
    <div class="feature" style="left:20px;top:12px">
      <div class="feature-icon"><svg viewBox="0 0 24 24"><rect x="3" y="5" width="18" height="14" rx="1"/><path d="M9 10l-2 2 2 2M15 10l2 2-2 2"/></svg></div>
      <p>High Converting<br>Website</p>
    </div>
    <div class="feature" style="left:141px;top:12px">
      <div class="feature-icon"><svg viewBox="0 0 24 24"><rect x="4" y="4" width="16" height="16"/><path d="M7 17v-4M11 17v-7M15 17v-5"/></svg></div>
      <p>SEO &amp; Online<br>Listings Management</p>
    </div>
    <div class="feature" style="left:262px;top:12px">
      <div class="feature-icon"><svg viewBox="0 0 24 24"><rect x="3" y="5" width="18" height="13"/><path d="M8 14l3-4 3 3 3-4"/></svg></div>
      <p>Strategic<br>PPC Advertising</p>
    </div>
    <div class="feature" style="left:369px;top:12px">
      <div class="feature-icon"><svg viewBox="0 0 24 24"><rect x="4" y="6" width="16" height="12"/><path d="M4 6l8 7 8-7"/></svg></div>
      <p>Email Marketing<br>and Automation</p>
    </div>
    <div class="feature" style="left:20px;top:102px">
      <div class="feature-icon"><svg viewBox="0 0 24 24"><circle cx="12" cy="12" r="3"/><circle cx="5" cy="6" r="2"/><circle cx="19" cy="6" r="2"/><circle cx="5" cy="18" r="2"/><circle cx="19" cy="18" r="2"/><path d="M7 7l3 3M17 7l-3 3M7 17l3-3M17 17l-3-3"/></svg></div>
      <p>Social Media<br>Management</p>
    </div>
    <div class="feature" style="left:141px;top:102px">
      <div class="feature-icon"><svg viewBox="0 0 24 24"><path d="M4 12a8 8 0 0 1 14-5M20 12a8 8 0 0 1-14 5"/><path d="M18 3v4h-4M6 21v-4h4"/></svg></div>
      <p>Retargeting<br>Campaigns</p>
    </div>
    <div class="feature" style="left:262px;top:102px">
      <div class="feature-icon"><svg viewBox="0 0 24 24"><path d="M12 3l2.6 5.4 5.9.8-4.3 4.1 1 5.8L12 16.3 6.8 19.1l1-5.8L3.5 9.2l5.9-.8z"/></svg></div>
      <p>Reputation<br>Management</p>
    </div>
    <div class="feature" style="left:369px;top:102px">
      <div class="feature-icon"><svg viewBox="0 0 24 24"><rect x="4" y="3" width="16" height="18"/><path d="M8 16v-3M12 16v-6M16 16v-4"/></svg></div>
      <p>Tracking<br>and Reporting</p>
    </div>
  </div>

  <footer class="abs footer">
    <div class="footer-cta"><span>GET STARTED NOW</span></div>
    <div class="footer-contact">
      <span><svg viewBox="0 0 24 24"><path d="M5 3h4l2 5-3 2a12 12 0 0 0 6 6l2-3 5 2v4a2 2 0 0 1-2 2A18 18 0 0 1 3 5a2 2 0 0 1 2-2z"/></svg>(555) 014-2290</span>
      <span><svg viewBox="0 0 24 24"><rect x="3" y="6" width="18" height="12"/><path d="M3 6l9 7 9-7"/></svg>hello@summitbn.com</span>
    </div>
  </footer>
</section>

<section class="page page--back">
  <div class="abs back-top"></div>
  <div class="abs back-top-right"></div>
  <p class="abs question">Does your<br><b>Business Struggle with Building a Steady Flow of qualified leads</b> using outdated marketing methods that <b>Just don’t work?</b></p>
  <div class="abs first-step">Take The Perfect First Step<br>TO GROW YOUR BUSINESS.</div>
  <div class="abs checklist-art" role="img" aria-label="Illustration of a spiral-bound marketing checklist booklet with a cartoon builder in a hard hat and a thumbs-up badge"></div>

  <div class="abs mission">
    <p>We Help General Contractors Implement A Results-Driven Online Marketing System That Is Proven To Generate The Highest-Quality Leads, Convert Those Leads Into Customers, And Ultimately... Increase Your Revenue.</p>
  </div>
  <div class="abs how-tab">How Do We Do It?</div>

  <div class="abs steps">
    <div class="step-art" style="top:14px;background:linear-gradient(160deg,#e9c95a,#c9a23a 60%,#f0f0f0)" role="img" aria-label="Illustration of a leaking sales funnel"></div>
    <div class="step-divider" style="top:20px;height:82px"></div>
    <div class="step" style="top:33px">
      <h3>Analyze Where Your<br>Funnel/Website Is Leaking Customers</h3>
      <p>We Take A Deep Dive Into Your Current Marketing System,<br>Website And Process.</p>
    </div>

    <div class="step-art" style="top:102px;background:linear-gradient(160deg,#f5f5f5,#cfe2d3 50%,#e8d9a8)" role="img" aria-label="Illustration of marketing blueprint documents"></div>
    <div class="step-divider" style="top:106px;height:92px"></div>
    <div class="step" style="top:115px">
      <h3>Get A Customized<br>Marketing Blueprint</h3>
      <p>We Work With You To Make Sure You Understand<br>The Key Things You'll Need To Do To Achieve<br>Your Business Goals.</p>
    </div>

    <div class="step-art" style="top:190px;background:linear-gradient(160deg,#e6c350,#3a5fa0 55%,#d8a23a)" role="img" aria-label="Illustration of a funnel and magnet attracting a team of builders"></div>
    <div class="step-divider" style="top:190px;height:82px"></div>
    <div class="step" style="top:198px">
      <h3>Take Your Business To<br>The Next Level</h3>
      <p>We Implement The Blueprint To Generate<br>More Revenue With An Online Marketing<br>&amp; Lead Generation System</p>
    </div>
  </div>

  <div class="abs portrait" role="img" aria-label="Photo of the company founder in a dark polo shirt with arms crossed"></div>
  <div class="abs ready condensed">Are you ready <em>to build and grow your business?</em></div>

  <footer class="abs footer">
    <div class="footer-cta"><span>GET STARTED NOW</span></div>
    <div class="footer-contact">
      <span><svg viewBox="0 0 24 24"><path d="M5 3h4l2 5-3 2a12 12 0 0 0 6 6l2-3 5 2v4a2 2 0 0 1-2 2A18 18 0 0 1 3 5a2 2 0 0 1 2-2z"/></svg>(555) 014-2290</span>
      <span><svg viewBox="0 0 24 24"><rect x="3" y="6" width="18" height="12"/><path d="M3 6l9 7 9-7"/></svg>hello@summitbn.com</span>
    </div>
  </footer>
</section>

</body>
</html>
```